Biotech company website design

We are looking for innovative design of our upcoming website. We are a small biotechnology company in Europe dealing with life science products and services.
Updates

Please incorporate the following top level links:
ABOUT US, PRODUCTS, SERVICES, SUPPLIERS, NEWS AND PROMOS, CONTACT US

Target Market(s)

Science people, hospitals, universities ....

Industry/Entity Type

It Company

Requirements
Must have
• Must incorporate our current logo (its color toning)

```html
<!DOCTYPE html>
<html lang="en">
<head>
<meta charset="utf-8">
<title>Meridian LifeLabs</title>
<link href="https://fonts.googleapis.com/css2?family=Arimo:wght@400;700&display=swap" rel="stylesheet">
<style>
  :root {
    --bg-top: #9fcfd6;
    --bg-bottom: #f1f1ea;
    --white: #ffffff;
    --panel: #f0f5f3;
    --green: #4c9a1c;
    --green-light: #8cc21e;
    --text: #666666;
    --dark: #2b2b2b;
    --muted: #9a9a9a;
    --divider: #b9b9b9;
  }
  * { margin: 0; padding: 0; box-sizing: border-box; }
  html, body { width: 1200px; height: 1060px; overflow: hidden; }
  body {
    position: relative;
    font-family: "Arimo", Arial, sans-serif;
    color: var(--text);
    background: linear-gradient(to bottom, var(--bg-top) 0, #c7e0df 380px, #e6ece4 640px, var(--bg-bottom) 1060px);
  }
  body::before {
    content: ""; position: absolute; left: 0; top: 0; width: 1200px; height: 3px; background: #7fbfc8;
  }
  .box { position: absolute; left: 96px; width: 1000px; background: var(--white); }

  .brand {
    position: absolute; display: flex; align-items: center; gap: 8px;
    font-size: 20px; font-weight: 400; color: var(--dark); letter-spacing: -0.2px;
  }
  .brand-mark { width: 22px; height: 22px; background: var(--green-light); }

  .site-header { top: 21px; height: 64px; }
  .site-header .brand { left: 20px; top: 20px; }
  .main-nav { position: absolute; right: 22px; top: 27px; display: flex; gap: 17px; }
  .main-nav a, .footer-nav a {
    font-size: 12.5px; font-weight: 700; color: var(--dark); text-decoration: none; letter-spacing: 0.3px;
  }
  .main-nav a.active { padding: 0 4px 3px; border-bottom: 2px solid var(--green); margin-left: -4px; margin-right: -4px; }

  .hero { top: 92px; height: 333px; padding: 7px 9px; }
  .hero-photo {
    width: 982px; height: 317px;
    background: linear-gradient(100deg, #c9d3d8 0%, #e9eef0 25%, #dfe9ee 50%, #c9d7df 70%, #f0e6e6 100%);
  }

  .welcome { top: 433px; height: 192px; background: var(--panel); }
  h2 { font-size: 14px; font-weight: 700; color: var(--green); letter-spacing: 0.2px; }
  .welcome h2 { position: absolute; left: 29px; top: 25px; }
  .welcome p { position: absolute; left: 29px; top: 66px; width: 735px; font-size: 12px; line-height: 17px; }
  .read-more { color: #111; text-decoration: none; font-size: 12px; }
  .welcome-photo {
    position: absolute; left: 800px; top: 59px; width: 176px; height: 115px;
    background: linear-gradient(120deg, #dfe6ea 0%, #b9c7d2 50%, #eef1f3 100%);
  }

  .features { top: 625px; height: 288px; }
  .col { position: absolute; top: 0; height: 288px; }
  .col h2 { position: absolute; top: 23px; }
  .col-services { left: 30px; width: 288px; }
  .col-products { left: 370px; width: 296px; }
  .col-news { left: 702px; width: 280px; }
  .intro { position: absolute; top: 62px; font-size: 12px; line-height: 17px; width: 270px; }
  .service-list { position: absolute; left: 21px; top: 116px; list-style: none; font-size: 12px; }
  .service-list li { height: 25px; }
  .product-photo {
    position: absolute; left: 0; top: 102px; width: 258px; height: 136px;
    background: linear-gradient(135deg, #8fb4d6 0%, #bcd3e8 45%, #e3e8ec 75%, #c9b8b3 100%);
  }
  .divider { position: absolute; top: 62px; height: 178px; border-left: 1px dotted var(--divider); }
  .news-item { position: absolute; left: -4px; width: 270px; font-size: 12px; line-height: 17px; }
  .news-item time { display: block; font-size: 11px; color: #111; }
  .news-item .read-more { color: var(--text); }

  .site-footer { top: 920px; height: 100px; }
  .footer-nav { position: absolute; left: 31px; top: 27px; display: flex; gap: 17px; }
  .legal { position: absolute; left: 29px; top: 54px; font-size: 12px; line-height: 14px; color: var(--muted); }
  .site-footer .brand { right: 22px; top: 36px; }
</style>
</head>
<body>
  <header class="box site-header">
    <div class="brand"><span class="brand-mark"></span>Meridian LifeLabs</div>
    <nav class="main-nav">
      <a class="active" href="#">ABOUT US</a>
      <a href="#">PRODUCTS</a>
      <a href="#">SERVICES</a>
      <a href="#">SUPPLIERS</a>
      <a href="#">NEWS AND PROMOS</a>
      <a href="#">CONTACT US</a>
    </nav>
  </header>

  <section class="box hero">
    <div class="hero-photo" role="img" aria-label="Laboratory scientist in mask and goggles holding a sample tube beside filtration tubing"></div>
  </section>

  <section class="box welcome">
    <h2>WELCOME TO OUR WEBSITE</h2>
    <p>Sed ut perspiciatis unde omnis iste natus error sit voluptatem accusantium doloremque laudantium, totam rem eaque ipsa quae ab illo inventore veritatis et quasi architecto beatae vitae dicta sunt explicabo. Nemo enim ip voluptatem quia voluptas sit aspernatur aut odit aut fugit, sed quia consequuntur magni dolores eos qui ration voluptatem sequi nesciunt. Nemo enim ip voluptatem quia voluptas sit asperna tur aut odit aut fugit, sed quia consequuntur magni dolores eos qui ration voluptatem sequi nesciunt.<br><a class="read-more" href="#">Read more..</a></p>
    <div class="welcome-photo" role="img" aria-label="Researcher in safety glasses using a pipette"></div>
  </section>

  <section class="box features">
    <div class="col col-services">
      <h2>SERVICES</h2>
      <p class="intro">Sed ut perspiciatis unde omnis iste natus error sit voluptatem accusantium doloremque</p>
      <ul class="service-list">
        <li>Nemo enim ip voluptatem quia</li>
        <li>Voluptas sit aspernatur aut odit aut</li>
        <li>Fugit sed quia consequuntur</li>
        <li>Magni dolores eos qui ration</li>
      </ul>
    </div>
    <div class="divider" style="left:318px"></div>
    <div class="col col-products">
      <h2>PRODUCTS</h2>
      <p class="intro">Sed ut perspiciatis unde omnis iste natus error sit voluptatem accusantium doloremque</p>
      <div class="product-photo" role="img" aria-label="Gloved hands handling a small sample vial"></div>
    </div>
    <div class="divider" style="left:666px"></div>
    <div class="col col-news">
      <h2>NEWS &amp; PROMOS</h2>
      <article class="news-item" style="top:64px">
        <time>12.07.2013</time>
        Sed ut perspiciatis unde omnis iste natus error sit voluptatem accusantium doloremque<br>
        <a class="read-more" href="#">Read more..</a>
      </article>
      <article class="news-item" style="top:155px">
        <time>12.07.2013</time>
        Sed ut perspiciatis unde omnis iste natus error sit voluptatem accusantium doloremque<br>
        <a class="read-more" href="#">Read more..</a>
      </article>
    </div>
  </section>

  <footer class="box site-footer">
    <nav class="footer-nav">
      <a href="#">ABOUT US</a>
      <a href="#">PRODUCTS</a>
      <a href="#">SERVICES</a>
      <a href="#">SUPPLIERS</a>
      <a href="#">NEWS AND PROMOS</a>
      <a href="#">CONTACT US</a>
    </nav>
    <p class="legal">COPYRIGHT 2013. ALL RIGHTS RESERVED.<br>TERMS &amp; CONDITIONS &nbsp;- &nbsp;PRIVACY &nbsp; - &nbsp; DISCLAIMER</p>
    <div class="brand"><span class="brand-mark"></span>Meridian LifeLabs</div>
  </footer>
</body>
</html>
```